Kestrel Summit 2019 Enemies of the End-Times Church Flyer

We want a church conference flyer designed. We are looking for a professional, yet catchy design that uses our brand colors and logo creatively while communicating key information of the event effectively. <br/>The flyer must include all of the following:<br/>Title: Kestrel Summit 2019<br/>Topic: The Enemies of The End-Times Church <br/>Subtitles: <br/> -How the antichrist raises an army by social behavior engineering. <br/>-How the architects of modern social constructs escaped the church's radar. <br/>-The Holy Spirit's end-times agenda:<br/> The Knock-Out Punch!<br/>Speaker: Prophet Marcus Toliver <br/>Dates/time: December 27, 28 & 29 at 6pm<br/>Location: Halvorn Community Center <br/> 241 Pellham Street <br/> Portland, ME 04102<br/>Contact info: phone: 207-555-0148 <br/>email: contact@brookmeadow.example <br/> www.vutel.example<br/>*The flyer must also include a picture of the speaker and our Vutel logo <br/>Thanks, we look forward to seeing what you come up with!

Colors

Designer to choose colors to be used in the design.

Requirements
Must have
• The flyer must include all of the following:
• Title: Kestrel Summit 2019
• Topic: The Enemies of The End-Times Church
• Subtitles:
• -How the antichrist raises an army by social behavior engineering.
• -How the architects of modern social constructs escaped the church's radar.
• -The Holy Spirit's end-times agenda:
• The Knock-Out Punch!
• Speaker: Prophet Marcus Toliver
• Dates/time: December 27, 28 & 29 at 6pm
• Location: Halvorn Community Center
• 241 Pellham Street
• Portland, ME 04102
• Contact info: phone: 207-555-0148
• email: contact@brookmeadow.example
• www.vutel.example
• *The flyer must also include a picture of the speaker and our Vutel logo
Should not have
• Pictures of crosses or church buildings

```html
<!DOCTYPE html>
<html lang="en">
<head>
<meta charset="utf-8">
<title>Kestrel Summit 2019 – The Enemies of The End-Times Church</title>
<link rel="stylesheet" href="https://fonts.googleapis.com/css2?family=Montserrat:wght@300;400;600;700&family=Saira+Condensed:wght@600&display=swap">
<style>
  :root {
    --navy: #0b3459;
    --orange: #f29222;
    --rust: #d8732f;
    --white: #ffffff;
    --photo-dark: #3b3633;
    --photo-light: #c9cdd6;
  }
  * { margin: 0; padding: 0; box-sizing: border-box; }
  html, body { width: 848px; height: 1200px; overflow: hidden; background: var(--white); }
  .flyer {
    position: relative; width: 848px; height: 1200px; overflow: hidden;
    background: var(--white); font-family: "Montserrat", sans-serif; color: var(--navy);
  }
  .speaker-hero {
    position: absolute; left: 300px; top: 14px; width: 548px; height: 443px;
    background: linear-gradient(115deg, var(--rust) 0%, var(--rust) 38%, var(--photo-dark) 62%, #5a2a2a 100%);
    clip-path: polygon(8% 4%, 40% 0, 100% 0, 100% 100%, 32% 100%, 30% 58%, 0 38%);
  }
  .speaker-side {
    position: absolute; left: 0; top: 520px; width: 264px; height: 280px;
    background: linear-gradient(160deg, #b9a98f, var(--photo-light));
    clip-path: polygon(0 0, 82% 0, 100% 55%, 88% 100%, 0 100%);
  }
  .speaker-action {
    position: absolute; left: 622px; top: 752px; width: 226px; height: 348px;
    background: linear-gradient(200deg, #2b2b2e, #8c8f96 60%, var(--photo-light));
    clip-path: polygon(8% 4%, 100% 0, 100% 100%, 14% 100%, 6% 60%);
  }
  .brand { position: absolute; left: 42px; top: 118px; display: flex; align-items: center; gap: 12px; white-space: nowrap; }
  .brand-dot { width: 26px; height: 26px; border-radius: 50%; background: var(--orange); }
  .brand-name { font-weight: 600; font-size: 54px; letter-spacing: 2px; color: var(--navy); }
  .title-light {
    position: absolute; left: 28px; top: 212px; font-weight: 400; font-size: 94px; line-height: 1; white-space: nowrap;
  }
  .title-bold {
    position: absolute; left: 26px; top: 318px; font-weight: 700; font-size: 138px; line-height: 1;
    letter-spacing: 2px; white-space: nowrap;
  }
  .topic-band {
    position: absolute; left: 0; top: 457px; width: 629px; height: 63px; background: var(--orange);
    display: flex; align-items: center; padding-left: 37px; white-space: nowrap; overflow: hidden;
    font-family: "Saira Condensed", "Arial Narrow", sans-serif; font-weight: 600; font-size: 34px; color: var(--white);
  }
  .year {
    position: absolute; left: 632px; top: 444px; font-weight: 300; font-size: 84px; line-height: 1;
    color: var(--orange); white-space: nowrap;
  }
  .details { position: absolute; left: 336px; top: 530px; font-size: 20px; font-weight: 400; white-space: nowrap; }
  .details-row { display: flex; align-items: center; gap: 10px; }
  .details-row + .details-row { margin-top: 12px; align-items: flex-start; }
  .details svg { flex: none; }
  .time { margin-left: 16px; display: flex; align-items: center; gap: 10px; }
  .address { line-height: 23px; }
  .speaker-label { position: absolute; left: 270px; top: 634px; font-size: 34px; font-weight: 400; white-space: nowrap; }
  .speaker-name { position: absolute; left: 270px; top: 676px; font-size: 40px; font-weight: 700; white-space: nowrap; }
  .topics {
    position: absolute; left: 18px; top: 802px; list-style: none; font-size: 28px; font-weight: 400;
    line-height: 41.5px; width: 600px;
  }
  .topics li { position: relative; padding-left: 22px; }
  .topics li::before { content: "•"; position: absolute; left: 0; font-weight: 700; }
  .topics strong { font-weight: 700; }
  .contact-bar {
    position: absolute; left: 0; top: 1100px; width: 848px; height: 100px; background: var(--navy);
    color: var(--white);
  }
  .phone { position: absolute; left: 30px; top: 16px; display: flex; align-items: center; gap: 10px; white-space: nowrap; }
  .phone-number { font-weight: 700; font-size: 42px; letter-spacing: -0.5px; }
  .links { position: absolute; left: 486px; top: 18px; font-size: 18px; line-height: 37px; white-space: nowrap; }
  .links div { display: flex; align-items: center; gap: 12px; }
</style>
</head>
<body>
<div class="flyer">
  <div class="speaker-hero" role="img" aria-label="Portrait of the speaker on an orange paint splash"></div>

  <div class="brand">
    <span class="brand-dot"></span>
    <span class="brand-name">VUTEL</span>
  </div>

  <div class="title-light">Kestrel</div>
  <div class="title-bold">SUMMIT</div>

  <div class="topic-band">The Enemies of The End-Times Church</div>
  <div class="year">2019</div>

  <div class="speaker-side" role="img" aria-label="Photo of the speaker preaching"></div>

  <div class="details">
    <div class="details-row">
      <svg width="34" height="34" viewBox="0 0 34 34" fill="none" stroke="currentColor" stroke-width="2">
        <rect x="2" y="5" width="26" height="24" rx="3"/><line x1="2" y1="12" x2="28" y2="12"/>
        <line x1="9" y1="2" x2="9" y2="8"/><line x1="21" y1="2" x2="21" y2="8"/>
        <circle cx="27" cy="27" r="6" fill="#fff"/><polyline points="24,27 26.5,29.5 30,25"/>
      </svg>
      <span>December 27, 28 &amp; 29</span>
      <span class="time">
        <svg width="28" height="32" viewBox="0 0 28 32" fill="none" stroke="currentColor" stroke-width="3">
          <circle cx="14" cy="18" r="11"/><line x1="10" y1="3" x2="18" y2="3"/><polyline points="14,12 14,18 18,20"/>
        </svg>
        6 pm
      </span>
    </div>
    <div class="details-row">
      <svg width="40" height="42" viewBox="0 0 40 42" fill="none" stroke="currentColor" stroke-width="2.4">
        <path d="M20 30 C12 20 9 16 9 12 a11 11 0 0 1 22 0 c0 4 -3 8 -11 18z"/><circle cx="20" cy="12" r="4"/>
        <path d="M13 30 L3 35 L20 41 L37 35 L27 30"/>
      </svg>
      <div class="address">Halvorn Community Center<br>241 Pellham Street Portland, ME 04102</div>
    </div>
  </div>

  <div class="speaker-label">Speaker:</div>
  <div class="speaker-name">Prophet Marcus Toliver</div>

  <div class="speaker-action" role="img" aria-label="Photo of the speaker gesturing at the pulpit"></div>

  <ul class="topics">
    <li>How the antichrist raises an army by social behavior engineering.</li>
    <li>How the architects of modern social con-struct escaped the church’s radar.</li>
    <li>The Holy Spirit’s end-times agenda:</li>
    <li>The <strong>Knock - Out Punch!</strong></li>
  </ul>

  <div class="contact-bar">
    <div class="phone">
      <svg width="74" height="66" viewBox="0 0 74 66" fill="none">
        <path d="M14 14 c-8 4 -10 12 -4 24 c6 12 16 22 26 24 c6 1 9 -2 10 -6 l-8 -8 c-2 2 -5 3 -8 1 c-5 -4 -9 -9 -11 -15 c-1 -3 1 -5 3 -6z" fill="var(--orange)"/>
        <rect x="36" y="2" width="36" height="24" rx="3" fill="var(--orange)"/>
        <path d="M42 26 l-4 8 l10 -8z" fill="var(--orange)"/>
        <circle cx="46" cy="14" r="2.5" fill="var(--navy)"/><circle cx="54" cy="14" r="2.5" fill="var(--navy)"/><circle cx="62" cy="14" r="2.5" fill="var(--navy)"/>
      </svg>
      <span class="phone-number">207-555-0148</span>
    </div>
    <div class="links">
      <div>
        <svg width="32" height="24" viewBox="0 0 32 24" fill="none" stroke="var(--orange)" stroke-width="2">
          <rect x="1" y="1" width="30" height="22"/><polyline points="1,1 16,14 31,1"/>
        </svg>
        contact@brookmeadow.example
      </div>
      <div>
        <svg width="32" height="30" viewBox="0 0 32 30" fill="none" stroke="var(--orange)" stroke-width="2">
          <circle cx="14" cy="14" r="12"/><ellipse cx="14" cy="14" rx="5" ry="12"/>
          <line x1="2" y1="14" x2="26" y2="14"/><path d="M20 18 l10 4 l-4 2 l-2 4z" fill="var(--orange)"/>
        </svg>
        www.vutel.example
      </div>
    </div>
  </div>
</div>
</body>
</html>
```